KFZ-Gutachter Banner

Ziel des Banners:
Der Banner soll auf die Tätigkeit als Kfz-Sachverständiger aufmerksam machen. Er wird im Außenbereich eingesetzt und soll schon aus der Ferne verständlich und gut lesbar sein.

Gestaltung:
• Schlichtes, professionelles Design (keine überladene Gestaltung, ruhige Farbwahl – anlehnend an den Farben schwarz und Rot.
• Ein Bild wo sich zwei hochwertige Autos verunfallt befinden
• Großzügige Schriftgrößen – der Text muss auch aus 20–30 m Entfernung gut lesbar sein
• Klare Informationsstruktur

Inhalte (Text):
1. Überschrift / Hauptaussage (groß & auffällig):
Kfz-Sachverständiger
oder
Unfallgutachten vom Profi
2. Kurze Beschreibung (kleiner, aber lesbar):
• Unfallgutachten
• Fahrzeugbewertung
• Technische Beratung
3. Kontaktdaten (am wichtigsten – sehr gut sichtbar & lesbar):
• Telefonnummer (z. B. groß & fett)
• Website oder E-Mail
• Optional: Standort oder “auch mobil im Einsatz”

Bildelemente:
• Optional ein dezentes Symbol oder Icon (z. B. Auto, Lupe, Checkzeichen) – nur wenn es nicht vom Text ablenkt

Format:
• Querformat, je nach Platz vor Ort (z. B. 3 m x 1,5 m)

Ingenieurbüro Tilo Marquardt Hofacker Str.14 58231 Menden www.pruefwerk-lo.de

• Man muss sofort erkennen, dass es sich um einen KFZ-Gutachter handelt.

```html
<!DOCTYPE html>
<html lang="de">
<head>
<meta charset="utf-8">
<title>Unfallgutachten Banner</title>
<link rel="stylesheet" href="https://fonts.googleapis.com/css2?family=Poppins:wght@300;400;600;700;800&display=swap">
<style>
  :root {
    --black: #000000;
    --red: #d9062b;
    --red-dark: #8f0a1e;
    --white: #ffffff;
    --photo-warm: #b86a4a;
    --photo-mid: #8c8a86;
    --photo-light: #d9d6d2;
  }
  * { margin: 0; padding: 0; box-sizing: border-box; }
  html, body { width: 1200px; height: 600px; overflow: hidden; background: var(--white); }
  .banner {
    position: relative;
    width: 1200px;
    height: 600px;
    background: var(--black);
    font-family: "Poppins", sans-serif;
    color: var(--white);
    overflow: hidden;
  }
  .photo {
    position: absolute;
    left: 0; top: 237px;
    width: 1200px; height: 271px;
    background: linear-gradient(90deg, var(--photo-warm) 0%, #a27a66 22%, var(--photo-mid) 45%, #6e6a66 60%, var(--photo-light) 82%, #a49a90 100%);
  }
  .shapes { position: absolute; inset: 0; }
  .brand {
    position: absolute;
    left: 20px; top: 40px;
    width: 260px;
    text-align: center;
  }
  .brand-dot {
    display: block;
    width: 86px; height: 86px;
    margin: 0 auto 18px;
    border: 3px solid var(--white);
    border-radius: 50%;
  }
  .brand-name {
    font-weight: 400;
    font-size: 24px;
    letter-spacing: 2px;
    white-space: nowrap;
  }
  .title {
    position: absolute;
    left: 316px; top: 146px;
    width: 830px;
    font-weight: 300;
    font-size: 41px;
    letter-spacing: 0.5px;
    white-space: nowrap;
    text-align: center;
  }
  .headline {
    position: absolute;
    left: 104px; top: 222px;
    width: 1001px;
    text-align: center;
    font-size: 58px;
    line-height: 72px;
    white-space: nowrap;
  }
  .headline strong { font-weight: 800; }
  .headline span { font-weight: 400; }
  .web {
    position: absolute;
    left: 153px; top: 522px;
    font-weight: 700;
    font-size: 42px;
    line-height: 60px;
  }
  .phone {
    position: absolute;
    left: 690px; top: 520px;
    width: 470px;
    text-align: center;
    font-weight: 500;
    font-size: 46px;
    line-height: 64px;
    white-space: nowrap;
  }
</style>
</head>
<body>
<div class="banner">
  <div class="photo" role="img" aria-label="Foto: zwei verunfallte Autos und ein Klemmbrett mit Schadensformular"></div>

  <svg class="shapes" width="1200" height="600" viewBox="0 0 1200 600">
    <!-- title rules -->
    <rect x="295" y="138" width="2" height="68" fill="var(--red)"/>
    <rect x="299" y="138" width="1.5" height="68" fill="var(--red)"/>
    <rect x="1155" y="138" width="2" height="68" fill="var(--red)"/>
    <rect x="1159" y="138" width="1.5" height="68" fill="var(--red)"/>
    <!-- headline ribbon -->
    <polygon points="104,215 96,237 112,237" fill="var(--red-dark)"/>
    <polygon points="1105,215 1113,237 1097,237" fill="var(--red-dark)"/>
    <polygon points="104,215 1105,215 1084,300 124,300" fill="var(--red)"/>
    <!-- contact bar -->
    <rect x="618" y="502" width="582" height="6" fill="var(--white)"/>
    <polygon points="0,508 598,508 636,554 598,600 0,600" fill="var(--red)"/>
    <polyline points="608,508 646,554 608,600" fill="none" stroke="var(--white)" stroke-width="5"/>
    <!-- globe icon -->
    <g class="globe-icon" fill="none" stroke="var(--white)">
      <circle cx="93" cy="554" r="31" fill="var(--white)" stroke="none"/>
      <circle cx="92" cy="553" r="24" stroke="var(--black)" stroke-width="3.5"/>
      <ellipse cx="92" cy="553" rx="10" ry="24" stroke="var(--black)" stroke-width="3"/>
      <line x1="68" y1="553" x2="116" y2="553" stroke="var(--black)" stroke-width="3"/>
      <rect x="72" y="546" width="40" height="13" fill="var(--white)" stroke="none"/>
      <text x="92" y="557" font-family="Poppins, sans-serif" font-size="10" font-weight="700" fill="var(--black)" stroke="none" text-anchor="middle">www</text>
      <polygon points="108,565 122,579 115,579 118,586 114,587 111,581 106,584" fill="var(--black)" stroke="var(--white)" stroke-width="1.5"/>
    </g>
  </svg>

  <div class="brand">
    <span class="brand-dot"></span>
    <div class="brand-name">TILO MARQUARDT</div>
  </div>

  <h1 class="title">KFZ-SACHVERSTÄNDIGER INGENIEURBÜRO</h1>

  <h2 class="headline"><strong>UNFALLGUTACHTEN</strong> <span>VOM PROFI</span></h2>

  <div class="web">pruefwerk-lo.de</div>
  <div class="phone">+49 172 318 40 96</div>
</div>
</body>
</html>
```